engaging mobile application to encourage lifestyle change

We need an App that will help people get from Bloom 4 Joy. A weight loss program based on realistic and healthy lifestyle modifications. By learning portion control, healthy food choices, and with the encouragement to get moving.
We would like the design to be gender neutral but must be fun.
The final design must be easy to use and useful to our clients.

Target Market(s)

Health, Wellbeing, Weightloss

Industry/Entity Type

Weight

Font styles to use
Sans Serif

Requirements
Must have
• Hydration log, Weigh-ins with fat %, Food log, Location of meetings,lectures and weigh-ins, list of restaurants that comply with B4J, Fitness plan, Mall walk maps, daily motivational message.

```html
<!DOCTYPE html>
<html lang="en">
<head>
<meta charset="utf-8">
<title>Log Water</title>
<link rel="stylesheet" href="https://fonts.googleapis.com/css2?family=Montserrat:wght@300;400;500;600&display=swap">
<style>
  :root {
    --page-bg: #eef1f4;
    --navy: #0a3c8e;
    --ocean: #0a79c8;
    --sky: #0a9bda;
    --accent: #06a7ea;
    --band: #0568c2;
    --card-top: #ffffff;
    --card-bottom: #eef0f2;
    --ink: #1d1d1f;
    --muted: #555a60;
    --white: #ffffff;
    --divider: #e2e4e7;
  }
  * { box-sizing: border-box; margin: 0; padding: 0; }
  html, body {
    width: 862px; height: 1200px; overflow: hidden;
    background: var(--page-bg);
    font-family: "Montserrat", sans-serif;
  }
  .screen {
    position: absolute; left: 92px; top: 0;
    width: 677px; height: 1200px; overflow: hidden;
    background: linear-gradient(180deg, var(--navy) 0%, var(--ocean) 30%, var(--sky) 60%, var(--sky) 100%);
    color: var(--white);
  }
  .status-bar { position: absolute; top: 8px; left: 0; right: 0; height: 30px; font-size: 22px; }
  .status-bar .signal { position: absolute; left: 16px; top: 7px; }
  .status-bar .clock { position: absolute; left: 0; right: 0; text-align: center; top: 0; }
  .status-bar .battery { position: absolute; right: 16px; top: 1px; display: flex; align-items: center; gap: 8px; }
  .nav-bar .title { position: absolute; top: 56px; width: 100%; text-align: center; font-size: 30px; font-weight: 500; }
  .nav-bar .date { position: absolute; top: 100px; width: 100%; text-align: center; font-size: 19px; }
  .nav-bar .back { position: absolute; left: 40px; top: 58px; }
  .nav-bar .confirm { position: absolute; left: 594px; top: 58px; }
  .card {
    position: absolute; left: 30px; top: 245px; width: 614px; height: 763px;
    background: var(--card-bottom);
    box-shadow: 0 2px 6px rgba(0,0,0,0.15);
  }
  .card-band { height: 29px; background: var(--band); }
  .summary {
    height: 353px; position: relative;
    background: linear-gradient(180deg, var(--card-top), var(--card-bottom));
    border-bottom: 1px solid var(--divider);
  }
  .label { position: absolute; top: 90px; font-size: 22px; line-height: 28px; color: var(--ink); transform: translateX(-50%); white-space: nowrap; }
  .label.logged { left: 163px; }
  .label.add-new { left: 458px; }
  .body-level {
    position: absolute; left: 129px; top: 137px; width: 69px; height: 168px;
    border-radius: 30px 30px 8px 8px;
    background: linear-gradient(180deg, #dcdfe3 0%, #dcdfe3 30%, #5fc8f2 42%, #0a6bb8 62%, #0a5aa6 100%);
  }
  .plus-sign { position: absolute; left: 308px; top: 196px; font-size: 40px; line-height: 48px; font-weight: 300; color: var(--ink); transform: translateX(-50%); }
  .glasses { position: absolute; left: 396px; top: 169px; }
  .volume { position: absolute; left: 458px; top: 251px; font-size: 20px; line-height: 26px; color: var(--muted); transform: translateX(-50%); }
  .counter { height: 282px; position: relative; background: linear-gradient(180deg, var(--card-top), var(--card-bottom)); border-bottom: 1px solid var(--divider); }
  .counter .heading { position: absolute; left: 37px; top: 35px; font-size: 29px; line-height: 36px; font-weight: 500; color: var(--ink); }
  .stepper { position: absolute; left: 0; right: 0; top: 136px; height: 60px; }
  .step-btn { position: absolute; top: 0; width: 60px; height: 60px; border-radius: 50%; background: var(--accent); }
  .step-btn.minus { left: 173px; }
  .step-btn.plus { left: 380px; }
  .step-btn::before, .step-btn.plus::after {
    content: ""; position: absolute; left: 19px; top: 27px; width: 22px; height: 6px; border-radius: 3px; background: var(--white);
  }
  .step-btn.plus::after { width: 6px; height: 22px; left: 27px; top: 19px; }
  .count { position: absolute; left: 307px; top: 0; transform: translateX(-50%); font-size: 72px; line-height: 60px; font-weight: 300; color: var(--ink); }
  .time-row { height: 99px; position: relative; background: linear-gradient(180deg, var(--card-top), var(--card-bottom)); }
  .time-row .heading { position: absolute; left: 37px; top: 34px; font-size: 29px; line-height: 36px; font-weight: 500; color: var(--ink); }
  .time-row .value { position: absolute; right: 59px; top: 36px; font-size: 26px; line-height: 32px; color: var(--muted); }
  .time-row .chevron { position: absolute; right: 28px; top: 47px; }
  .drop-badge {
    position: absolute; left: 266px; top: 171px; width: 144px; height: 144px; border-radius: 50%;
    background: var(--accent); box-shadow: 0 3px 6px rgba(0,0,0,0.2);
    display: flex; align-items: center; justify-content: center;
  }
</style>
</head>
<body>
<main class="screen">
  <div class="status-bar">
    <svg class="signal" width="90" height="16" viewBox="0 0 90 16" aria-hidden="true">
      <g fill="#fff"><circle cx="6" cy="8" r="5"/><circle cx="19" cy="8" r="5"/><circle cx="32" cy="8" r="5"/><circle cx="45" cy="8" r="5"/></g>
      <circle cx="58" cy="8" r="4.3" fill="none" stroke="#fff" stroke-width="1.4"/>
      <path d="M71 5 a12 12 0 0 1 16 0 M74 9 a7 7 0 0 1 10 0" fill="none" stroke="#fff" stroke-width="2"/>
      <circle cx="79" cy="13" r="2" fill="#fff"/>
    </svg>
    <div class="clock">11:14 PM</div>
    <div class="battery">100%
      <svg width="52" height="22" viewBox="0 0 52 22" aria-hidden="true">
        <rect x="1" y="1" width="46" height="20" rx="4" fill="none" stroke="#fff" stroke-width="2"/>
        <rect x="4" y="4" width="40" height="14" rx="2" fill="#fff"/>
        <rect x="48" y="7" width="3" height="8" rx="1" fill="#fff"/>
      </svg>
    </div>
  </div>

  <header class="nav-bar">
    <svg class="back" width="24" height="40" viewBox="0 0 24 40" aria-label="Back"><path d="M20 4 L5 20 L20 36" fill="none" stroke="#fff" stroke-width="3.5" stroke-linecap="round" stroke-linejoin="round"/></svg>
    <h1 class="title">Log Water</h1>
    <p class="date">February 15, 2016</p>
    <svg class="confirm" width="46" height="40" viewBox="0 0 46 40" aria-label="Save"><path d="M4 22 L16 34 L42 6" fill="none" stroke="#fff" stroke-width="4" stroke-linecap="round" stroke-linejoin="round"/></svg>
  </header>

  <section class="card">
    <div class="card-band"></div>
    <div class="summary">
      <span class="label logged">You’ve logged</span>
      <div class="body-level" role="img" aria-label="Figure filled to show the water logged today"></div>
      <span class="plus-sign">+</span>
      <span class="label add-new">Add new</span>
      <svg class="glasses" width="124" height="62" viewBox="0 0 124 62" aria-hidden="true">
        <path d="M2 2 H52 L47 60 H7 Z" fill="#0a5aa6"/>
        <path d="M8 12 L30 8 L46 4 L42 54 H11 Z" fill="#2bb7f0"/>
        <path d="M72 2 H122 L117 60 H77 Z" fill="#0a5aa6"/>
        <path d="M78 12 L100 8 L116 4 L112 54 H81 Z" fill="#2bb7f0"/>
      </svg>
      <span class="volume">500 ml</span>
    </div>
    <div class="counter">
      <h2 class="heading">Number of glasses</h2>
      <div class="stepper">
        <span class="step-btn minus" aria-label="Fewer glasses"></span>
        <span class="count">2</span>
        <span class="step-btn plus" aria-label="More glasses"></span>
      </div>
    </div>
    <div class="time-row">
      <h2 class="heading">Time</h2>
      <span class="value">Today 18:25</span>
      <svg class="chevron" width="16" height="10" viewBox="0 0 16 10" aria-hidden="true"><path d="M2 2 L8 8 L14 2" fill="none" stroke="#06a7ea" stroke-width="2.2" stroke-linecap="round"/></svg>
    </div>
  </section>

  <div class="drop-badge">
    <svg width="64" height="86" viewBox="0 0 64 86" aria-label="Water drop">
      <path d="M32 2 C32 2 4 40 4 56 A28 28 0 0 0 60 56 C60 40 32 2 32 2 Z" fill="#fff"/>
      <path d="M16 56 A16 16 0 0 0 34 72" fill="none" stroke="#06a7ea" stroke-width="5" stroke-linecap="round"/>
    </svg>
  </div>
</main>
</body>
</html>
```